Minimalist Professional Business Card Design

We will be revamping our marketing materials: Business cards, Website and Catalogs.
Our Overall Design direction is to have a Minimalist artwork with Professionalism and Premium feel. The revamp starts with the new business card design followed by the others. Thus the designer whom work is selected for this job will likely to follow through with the subsequent jobs.

Target Market(s)

Upscale

Industry/Entity Type

Manufacturing

Contact Information for Business Card

For the Business Cards, the following are required:
. Minimalist yet Professional and Premium Feel
. Background Colors: white and / or light pastel yellow and if needed to smoothen the yellow, the light grey can be incorporated. We are changing our corporate bright yellow to either one of the three alternatives:
1. Soylant yellow CMYK (1%, 0%, 52%, 3%)
2. Popcorn yellow CMYK (0%, 0%, 33%, 0%)
3. Papaya yellow CMYK (0%, 0%, 51%, 0%)

Information to be inputed in the business cards:

Name: Barlen Moritova
Position: Managing Director

Company's name: Vellomar Valves Pte. Ltd.
Address: 512 Halvick Lane #07-09B
Singapore 617302
Tel: (65) 6281 4096
Fax: (65) 6294 7118
Email: barlen@vellomarvalves-example.com
Website: www.vellomarvalves-example.com
Talkora: Vellomar.Valves
Messly/ Chirpa/ Ringlo/ Yapper: (65) 9372 6081

Company's Logo
Company's Slogan
Two product photos placed side by side (if this gets into the way of the design, it is OK not to include them)

Font styles to use
Serif

Colors
ffffff

Requirements
Must have
• Minimalist
Should not have
• Messy, crowded, playful

```html
<!DOCTYPE html>
<html lang="en">
<head>
<meta charset="utf-8">
<title>Vellomar Valves – Business Card</title>
<link href="https://fonts.googleapis.com/css2?family=Jost:wght@400;500;600;700&family=Montserrat:wght@400;500;600&display=swap" rel="stylesheet">
<style>
  :root {
    --backdrop: #b1b1b1;
    --paper: #ececec;
    --ink: #565656;
    --charcoal: #363636;
    --band-grey: #5b5b5b;
    --pastel-yellow: #ded885;
    --wave-yellow: #d9d36a;
    --wave-light: #e4df95;
    --light-text: #ededed;
  }
  * { margin: 0; padding: 0; box-sizing: border-box; }
  html, body { width: 1200px; height: 1157px; overflow: hidden; }
  body { background: var(--backdrop); position: relative; font-family: "Montserrat", sans-serif; }

  .card {
    position: absolute; left: 184px; width: 836px; height: 462px; overflow: hidden;
  }
  .card--front { top: 92px; background: var(--paper); }
  .card--back { top: 608px; background: var(--pastel-yellow); }

  .card__waves { position: absolute; inset: 0; }

  .holder { position: absolute; left: 62px; top: 80px; color: var(--ink); }
  .holder__name { font-family: "Jost", sans-serif; font-weight: 700; font-size: 32px; letter-spacing: 0.3px; line-height: 1; }
  .holder__title { font-family: "Jost", sans-serif; font-weight: 400; font-size: 20.5px; margin-top: 9px; }

  .brand { position: absolute; display: flex; flex-direction: column; align-items: center; color: var(--ink); }
  .brand__mark { border-radius: 50%; border: solid var(--ink); }
  .brand__name { font-family: "Jost", sans-serif; font-weight: 700; line-height: 1; letter-spacing: 0; }
  .card--front .brand { left: 516px; top: 70px; width: 260px; }
  .card--front .brand__mark { width: 144px; height: 144px; border-width: 12px; }
  .card--front .brand__name { font-size: 44px; margin-top: 28px; }
  .card--back .brand { left: 282px; top: 50px; width: 260px; }
  .card--back .brand__mark { width: 164px; height: 164px; border-width: 14px; }
  .card--back .brand__name { font-size: 50px; margin-top: 32px; }

  .contacts { position: absolute; left: 62px; top: 319px; list-style: none; color: var(--light-text); }
  .contacts__item { display: flex; align-items: center; height: 30.5px; font-size: 20.5px; }
  .contacts__icon { width: 20px; height: 20px; margin-right: 17px; flex: none; }

  .address { position: absolute; left: 0; right: 0; top: 342px; text-align: center; font-family: "Montserrat", sans-serif; font-weight: 600; font-size: 20.5px; color: var(--charcoal); }

  .messaging {
    position: absolute; left: 0; right: 0; bottom: 0; height: 64px; background: var(--band-grey);
    display: flex; align-items: center; justify-content: center; gap: 20px;
    color: var(--light-text); font-weight: 600; font-size: 19.5px;
  }
  .messaging__divider { font-weight: 400; }
</style>
</head>
<body>

<section class="card card--front">
  <svg class="card__waves" viewBox="0 0 836 462" aria-hidden="true">
    <path fill="var(--wave-light)" d="M30,248 C110,208 200,196 290,212 C390,230 470,290 560,330 C520,300 420,236 320,216 C220,198 120,214 30,248 Z"/>
    <path fill="var(--wave-yellow)" d="M0,300 C70,254 160,222 250,224 C370,228 470,304 580,346 C680,378 760,362 836,330 L836,380 C720,410 620,420 530,392 C430,356 330,278 220,274 C140,272 70,300 0,326 Z"/>
    <path fill="var(--charcoal)" d="M0,338 C80,292 150,266 220,270 C330,276 420,342 520,390 C600,424 700,414 836,384 L836,462 L0,462 Z"/>
  </svg>

  <div class="holder">
    <h1 class="holder__name">Barlen Moritova</h1>
    <p class="holder__title">Managing Director</p>
  </div>

  <div class="brand">
    <div class="brand__mark"></div>
    <div class="brand__name">VELLOMAR</div>
  </div>

  <ul class="contacts">
    <li class="contacts__item">
      <svg class="contacts__icon" viewBox="0 0 20 20"><circle cx="10" cy="10" r="9" fill="none" stroke="currentColor" stroke-width="1.3"/><path fill="currentColor" d="M6.4 5.2l1.6-.4 1.1 2.4-1 .8c.5 1.2 1.4 2.1 2.6 2.6l.8-1 2.4 1.1-.4 1.6c-3.8.3-7.4-3.3-7.1-7.1z"/></svg>
      (65) 6281 4096
    </li>
    <li class="contacts__item">
      <svg class="contacts__icon" viewBox="0 0 20 20"><circle cx="10" cy="10" r="9" fill="none" stroke="currentColor" stroke-width="1.3"/><path fill="currentColor" d="M6.4 5.2l1.6-.4 1.1 2.4-1 .8c.5 1.2 1.4 2.1 2.6 2.6l.8-1 2.4 1.1-.4 1.6c-3.8.3-7.4-3.3-7.1-7.1z"/></svg>
      (65) 6294 7118
    </li>
    <li class="contacts__item">
      <svg class="contacts__icon" viewBox="0 0 20 20"><circle cx="10" cy="10" r="9" fill="none" stroke="currentColor" stroke-width="1.3"/><rect x="5.5" y="7" width="9" height="6.5" fill="currentColor"/><path d="M5.5 7l4.5 3.5 4.5-3.5" fill="none" stroke="var(--charcoal)" stroke-width="1"/></svg>
      barlen@vellomarvalves-example.com
    </li>
    <li class="contacts__item">
      <svg class="contacts__icon" viewBox="0 0 20 20" fill="none" stroke="currentColor"><circle cx="10" cy="10" r="9" stroke-width="1.3"/><circle cx="10" cy="10" r="5" stroke-width="1"/><ellipse cx="10" cy="10" rx="2" ry="5" stroke-width="1"/><path d="M5 10h10" stroke-width="1"/></svg>
      www.vellomarvalves-example.com
    </li>
  </ul>
</section>

<section class="card card--back">
  <div class="brand">
    <div class="brand__mark"></div>
    <div class="brand__name">VELLOMAR</div>
  </div>
  <p class="address">512 Halvick Lane #07-09B, Singapore 617302</p>
  <div class="messaging">
    <span>Talkora: Vellomar.Valves</span>
    <span class="messaging__divider">|</span>
    <span>Messly/ Chirpa/ Ringlo/ Yapper: (65) 9372 6081</span>
  </div>
</section>

</body>
</html>
```